Mara Joss Advisory Business Cards

Hi - using the information and logo provided I require a two sided business card designed with the following information. The business card is a 'mini card' 3.5" x 1.25".

Front of card should be the logo attached but inverted (so the background is the peach colour and the logo white).

Back should have these details. If we can't fit the Instragram and Facebook part can we just put the little logos.

Ruth Penderby

Art and Design Consultant
Dealer - Curator - Events - Styling - Creative Sourcing

P: 0462 913 058
E: ruth@marajossadvisory.example
W: www.marajossadvisory.example
I (instagram image please): marajossadvisory F (Facebook image please): MaraJossAdvisor

Target Market(s)

Galleries, artists, art buyers, interior design clients, event managers, creative types

Industry/Entity Type

Business

```html
<!DOCTYPE html>
<html lang="en">
<head>
<meta charset="utf-8">
<title>Mara Joss Advisory – Mini Business Cards</title>
<link rel="stylesheet" href="https://fonts.googleapis.com/css2?family=Arimo:wght@400;700&display=swap">
<style>
  :root {
    --backdrop: #2a2a2b;
    --card-front-top: #6a6b6d;
    --card-front-bottom: #4e4f51;
    --card-back: #ffffff;
    --peach: #e39a7d;
    --ink: #3a3a3a;
    --ink-soft: #555555;
    --white: #ffffff;
  }
  * { box-sizing: border-box; margin: 0; padding: 0; }
  html, body {
    width: 1200px;
    height: 900px;
    overflow: hidden;
    background: var(--backdrop);
    font-family: "Arimo", Arial, sans-serif;
  }
  .canvas {
    width: 1200px;
    height: 900px;
    display: flex;
    flex-direction: column;
    align-items: center;
    justify-content: center;
    gap: 60px;
  }
  .card {
    width: 700px;
    height: 250px;
    position: relative;
    box-shadow: 0 12px 30px rgba(0,0,0,0.45);
  }

  /* Front */
  .card-front {
    background: linear-gradient(160deg, var(--card-front-top), var(--card-front-bottom));
    display: flex;
    align-items: center;
    justify-content: center;
  }
  .brand {
    display: flex;
    align-items: center;
    gap: 14px;
    font-weight: 400;
  }
  .brand-dot {
    width: 22px;
    height: 22px;
    border-radius: 50%;
  }
  .card-front .brand-name { color: var(--white); font-size: 30px; letter-spacing: 0.5px; }
  .card-front .brand-dot { background: var(--white); }

  /* Back */
  .card-back { background: var(--card-back); color: var(--ink); }
  .card-back .brand {
    position: absolute;
    top: 36px;
    right: 32px;
  }
  .card-back .brand-name { color: var(--peach); font-size: 17px; }
  .card-back .brand-dot { background: var(--peach); width: 16px; height: 16px; }
  .accent-rule {
    position: absolute;
    left: 28px;
    right: 250px;
    top: 94px;
    height: 1.5px;
    background: var(--peach);
  }
  .holder-name {
    position: absolute;
    left: 30px;
    top: 64px;
    font-size: 25px;
    color: var(--ink);
  }
  .holder-role {
    position: absolute;
    left: 30px;
    top: 100px;
    font-size: 14px;
    line-height: 17px;
    color: var(--ink-soft);
  }
  .contact-list {
    position: absolute;
    left: 30px;
    top: 150px;
    list-style: none;
    font-size: 10px;
    line-height: 14px;
    color: var(--ink-soft);
  }
  .contact-label { color: var(--peach); margin-right: 4px; }
  .social-row {
    position: absolute;
    left: 30px;
    right: 30px;
    bottom: 22px;
    display: flex;
    gap: 90px;
    font-size: 16px;
    color: var(--ink);
  }
  .social-handle { display: flex; align-items: center; gap: 10px; }
  .social-square {
    width: 22px;
    height: 22px;
    background: var(--ink);
    border-radius: 3px;
  }
</style>
</head>
<body>
<main class="canvas">
  <section class="card card-front" aria-label="Card front">
    <div class="brand">
      <span class="brand-dot"></span>
      <span class="brand-name">Mara Joss Advisory</span>
    </div>
  </section>

  <section class="card card-back" aria-label="Card back">
    <div class="brand">
      <span class="brand-dot"></span>
      <span class="brand-name">Mara Joss Advisory</span>
    </div>
    <h1 class="holder-name">Ruth Penderby</h1>
    <div class="accent-rule"></div>
    <p class="holder-role">Art and Design Consultant<br>Dealer - Curator - Events - Styling - Creative Sourcing</p>
    <ul class="contact-list">
      <li><span class="contact-label">P:</span>0462 913 058</li>
      <li><span class="contact-label">E:</span>ruth@marajossadvisory.example</li>
      <li><span class="contact-label">W:</span>www.marajossadvisory.example</li>
    </ul>
    <div class="social-row">
      <span class="social-handle"><span class="social-square"></span>marajossadvisory</span>
      <span class="social-handle"><span class="social-square"></span>MaraJossAdvisor</span>
    </div>
  </section>
</main>
</body>
</html>
```